Very Simple Web Redesign Project - Using Photoshop

Required is a very simple website home page redesign for the following site: http://www.tallowcrestslate.com.au/
I require this as a Photoshop design.
The basic look and feel of the site needs to remain.
Specifically the colours don't need to be changed.
The positioning of the site is currently correct for the target market.
The site does not need to be made super slick looking. Just upgraded to a new version.
The current text can all be used.
The only menus necessary are a horizontal menu at the top, and a simple horizontal text menu at the bottom of the page. Do NOT retain the vertical menu on the home page (having the items "Our Gallery", "Our Services", "Enquire Now").
Give the horizontal menu the following items:
Home | Slate Roof Repairs | Slate Reroofing | Slate Roof Benefits | Other Services | Photo Gallery | FAQ's | Free Quote | Contact Us
The picture of the house at the top RHS of the page needs to be reduced in size by approx 50% and moved to the top LHS of the page.
Please place the following text into the top of the page:
"Call Now: 0427 618 392"
Keep the four pictures on the home page layout. Some larger images attached.
Thanks,
Rob
Updates
Hi,
Thanks for all the designs.
I am working with my client to get which one they like the most.
Thanks,
Rob

```html
<!DOCTYPE html>
<html lang="en">
<head>
<meta charset="utf-8">
<title>Tallowcrest Slate - the Slate Roof Specialists</title>
<link rel="stylesheet" href="https://fonts.googleapis.com/css2?family=Tinos:wght@400;700&display=swap">
<style>
  :root {
    --green-dark: #2f6b12;
    --green-mid: #4a9221;
    --green-light: #5fae2e;
    --black: #000000;
    --white: #ffffff;
    --panel-grey: #857f80;
    --footer-grey: #dedbdc;
    --body-text: #4a4a4a;
    --rule: #6a6a6a;
    --heading: #1d1d1d;
    --quote-red: #b8262c;
  }
  * { box-sizing: border-box; margin: 0; padding: 0; }
  html, body { width: 1073px; height: 1200px; overflow: hidden; }
  body {
    position: relative;
    background: var(--white);
    font-family: "Tinos", "Times New Roman", serif;
  }
  .site-header {
    position: absolute; left: 0; top: 0; width: 1073px; height: 158px;
    background: linear-gradient(180deg, var(--green-mid) 10%, var(--green-dark) 100%);
    border-top: 7px solid #111;
  }
  .brand {
    position: absolute; left: 62px; top: 40px;
    display: flex; align-items: center; gap: 20px;
  }
  .brand-mark { width: 72px; height: 72px; background: #234f0e; }
  .brand-name { font-size: 50px; font-weight: 700; color: var(--white); }
  .call-now {
    position: absolute; right: 48px; top: 88px;
    display: flex; align-items: center; gap: 8px;
    color: var(--white); font-size: 18px; font-weight: 700;
  }
  .main-nav {
    position: absolute; left: 0; top: 160px; width: 1073px; height: 44px;
    background: linear-gradient(180deg, var(--green-light), var(--green-dark));
    border-top: 1px solid #8fd062; border-bottom: 2px solid #2a5a10;
  }
  .main-nav ul, .footer-nav ul { list-style: none; display: flex; }
  .main-nav ul { position: absolute; left: 70px; top: 6px; height: 32px; border-left: 1px solid #2a5a10; }
  .main-nav li {
    padding: 0 11px; line-height: 32px; font-size: 15px; color: var(--white);
    border-right: 1px solid #2a5a10;
  }
  .black-band { position: absolute; left: 0; top: 206px; width: 1073px; height: 325px; background: var(--black); }
  .banner {
    position: absolute; left: 70px; top: 218px; width: 880px; height: 226px;
    background: linear-gradient(180deg, var(--green-light), var(--green-dark));
    border: 2px solid #cfcfcf; border-radius: 3px;
  }
  .banner-photo { position: absolute; top: 6px; width: 276px; height: 206px; border: 3px solid #e9e9e9; }
  .footer-band { position: absolute; left: 0; top: 1092px; width: 1073px; height: 108px; background: var(--footer-grey); z-index: 1; }
  .content {
    position: absolute; left: 72px; top: 446px; width: 878px; height: 696px; z-index: 2;
    background: var(--white); border: 2px solid #cfcfcf; border-radius: 3px;
    box-shadow: 2px 3px 4px rgba(0,0,0,.35);
  }
  .sidebar {
    position: absolute; left: 4px; top: 4px; width: 346px; height: 686px;
    background: var(--panel-grey); color: var(--white);
  }
  .sidebar h2 { position: absolute; left: 16px; top: 18px; font-size: 20px; font-weight: 700; }
  .sidebar .service-area { position: absolute; left: 14px; top: 56px; width: 326px; font-size: 15px; line-height: 19px; }
  .quote-button {
    position: absolute; left: 34px; top: 154px; width: 200px; height: 102px;
    background: linear-gradient(180deg, #d3474c 0%, var(--quote-red) 40%, #2a0a0a 100%);
    border: 2px solid #eee; border-radius: 10px;
    display: flex; align-items: center; gap: 10px; padding-left: 30px;
    box-shadow: 0 0 6px rgba(0,0,0,.5);
  }
  .quote-button span { font-family: Arial, sans-serif; color: #f4b23a; font-size: 19px; line-height: 24px; }
  .contact-line {
    position: absolute; left: 22px; font-size: 20px; font-weight: 700;
    display: flex; align-items: center; gap: 6px;
  }
  .article { position: absolute; left: 362px; top: 0; width: 500px; height: 690px; }
  .article h1 { position: absolute; left: 4px; top: 18px; font-size: 24px; color: var(--heading); }
  .article .rule { position: absolute; left: 2px; width: 482px; border-top: 1px solid var(--rule); }
  .article p { position: absolute; left: 4px; width: 484px; font-size: 14px; line-height: 25px; color: var(--body-text); }
  .work-photo { position: absolute; top: 505px; width: 217px; height: 163px; border: 2px solid #555; }
  .footer-nav { position: absolute; left: 45px; top: 1163px; z-index: 3; }
  .footer-nav li { font-size: 15px; color: #333; margin-right: 28px; }
</style>
</head>
<body>
  <header class="site-header">
    <div class="brand">
      <div class="brand-mark"></div>
      <div class="brand-name">Tallowcrest Slate</div>
    </div>
    <div class="call-now">
      <svg width="26" height="26" viewBox="0 0 26 26" aria-hidden="true">
        <circle cx="13" cy="13" r="12" fill="#d63a2a" stroke="#fff" stroke-width="1.5"/>
        <path d="M9 7c1 0 2 2 2 3s-1 1-1 2 2 4 3 4 1-1 2-1 3 1 3 2-1 2-2 2c-4 0-9-6-9-10 0-1 1-2 2-2z" fill="#fff"/>
      </svg>
      Call Now: 0427 618 392
    </div>
  </header>

  <nav class="main-nav">
    <ul>
      <li>Home</li><li>Slate Roof Repairs</li><li>Slate Reroofing</li><li>Slate Roof Benefits</li>
      <li>Other Services</li><li>Photo Gallery</li><li>FAQ's</li><li>Free Quote</li><li>Contact Us</li>
    </ul>
  </nav>

  <div class="black-band"></div>

  <section class="banner">
    <div class="banner-photo" style="left:14px;background:linear-gradient(180deg,#8a9a7a 0%,#6f7a74 40%,#5f8a3a 75%,#7fae3e 100%);" role="img" aria-label="Slate-roofed garden gazebo among hedges"></div>
    <div class="banner-photo" style="left:300px;background:linear-gradient(180deg,#a8c0d8 0%,#6f7780 35%,#8a8c8e 65%,#5c6058 100%);" role="img" aria-label="Slate roof with a bay window turret"></div>
    <div class="banner-photo" style="left:586px;background:linear-gradient(160deg,#6a6c70 0%,#555862 50%,#8a6a58 85%,#9a7a66 100%);" role="img" aria-label="Slate roof with a dormer window"></div>
  </section>

  <div class="footer-band"></div>

  <main class="content">
    <aside class="sidebar">
      <h2>Call now and arrange a free quote</h2>
      <p class="service-area">We service all inner city suburbs of Sydney roughly covering an area encompassing Gordon to Epping, Mosman to Bondi, Coogee to Kogarah and Kingsgrove to Burwood and Concord</p>
      <div class="quote-button">
        <svg width="44" height="40" viewBox="0 0 44 40" aria-hidden="true">
          <path d="M3 22l10 12L41 4" fill="none" stroke="#1b1b1b" stroke-width="9" stroke-linecap="round" stroke-linejoin="round"/>
          <path d="M3 22l10 12L41 4" fill="none" stroke="#4caf2a" stroke-width="5" stroke-linecap="round" stroke-linejoin="round"/>
        </svg>
        <span>Get a free<br>Quote</span>
      </div>
      <div class="contact-line" style="top:330px">Mobile: 0427618392
        <svg width="18" height="26" viewBox="0 0 18 26" aria-hidden="true"><rect x="1" y="1" width="16" height="24" rx="3" fill="#222"/><rect x="3" y="4" width="12" height="16" fill="#5b7ea8"/></svg>
      </div>
      <div class="contact-line" style="top:378px">Fax: 02 94715063
        <svg width="32" height="26" viewBox="0 0 32 26" aria-hidden="true"><rect x="2" y="10" width="28" height="14" rx="3" fill="#9aa0a6"/><rect x="8" y="3" width="14" height="10" fill="#e8e8e8"/><rect x="5" y="13" width="8" height="4" fill="#6a7076"/></svg>
      </div>
      <div class="contact-line" style="top:474px">Abn 47 603 219 884</div>
      <div class="contact-line" style="top:522px">Lic No. 208417C</div>
    </aside>

    <article class="article">
      <h1>Tallowcrest Slate - the Slate Roof Specialists</h1>
      <div class="rule" style="top:93px"></div>
      <p style="top:101px">At Tallowcrest Slate we specialize in the upkeep, maintenance, repair and replacement of all types of slate roof as well as wood shingles.&nbsp; We can track down the leak that just won't go away or give your house a complete re-roof. We can also provide all your guttering needs.</p>
      <div class="rule" style="top:213px"></div>
      <p style="top:222px">Tallowcrest Slate is a small company and as such we do not have the overheads that larger companies do.&nbsp; Quality work and attention to detail are our trademark.</p>
      <div class="rule" style="top:288px"></div>
      <p style="top:296px">All photos on this website consist of work which I have personally done.&nbsp; The above photos provide at a quick glance a reasonable cross section of the type of work I do.</p>
      <div class="rule" style="top:362px"></div>
      <p style="top:370px">By clicking on the Photo Gallery link you can see other work including some before and after shots.</p>
      <div class="rule" style="top:435px"></div>
      <p style="top:443px">Feel free to call at your earliest convenience to organise an obligation free quote or fill out a form by clicking on the Contact Us link below.</p>
      <div class="work-photo" style="left:0;background:linear-gradient(160deg,#8a5a48 0%,#7a7e86 40%,#8c9096 80%,#6a6e72 100%);" role="img" aria-label="Slate roof beside a brick wall and balcony"></div>
      <div class="work-photo" style="left:226px;background:linear-gradient(160deg,#c8b890 0%,#6a6e78 35%,#5c606a 75%,#8a8e94 100%);" role="img" aria-label="New slate roof below a sash window"></div>
    </article>
  </main>

  <nav class="footer-nav">
    <ul>
      <li>Home</li><li>Slate Roof Repairs</li><li>Slate Reroofing</li><li>Slate Roof Benefits</li>
      <li>Other Services</li><li>Photo Gallery</li><li>FAQ's</li><li>Free Quote</li><li>Contact Us</li>
    </ul>
  </nav>
</body>
</html>
```